Lets get creative with Marlow Finance Brochure

I have used pixelforum before for a previous brochure which is attached business BRACKEN Automotive. I would like to work together on a new project MARLOW Finance. https://marlowfinance.com.au/
It is a boutique Finance company ideally targeting the small to Medium business s along with consumer finance. I have attached previous brochure to give an idea of layout. Once we have a layout i will send wording through.

Target Market(s)

business owners

Industry/Entity Type

Finance

Font styles to use
Serif

Colors
0355a3
fef3ec

```html
<!DOCTYPE html>
<html lang="en">
<head>
<meta charset="utf-8">
<title>Marlow Finance Tri-fold Brochure</title>
<link href="https://fonts.googleapis.com/css2?family=Playfair+Display:wght@600;700&family=Source+Serif+4:opsz,wght@8..60,400;8..60,600;8..60,700&display=swap" rel="stylesheet">
<style>
  :root{
    --page:#e9e7e5;
    --brand:#0355a3;
    --brand-deep:#023b72;
    --brand-light:#4f8fcf;
    --brand-mid:#2a73bb;
    --cream:#fef3ec;
    --ink:#1e2430;
    --white:#ffffff;
  }
  *{box-sizing:border-box;margin:0;padding:0}
  html,body{width:1200px;height:1200px;overflow:hidden}
  body{background:var(--page);font-family:"Source Serif 4",Georgia,serif;color:var(--ink);position:relative}

  .spread-label{position:absolute;top:620px;font-size:13px;letter-spacing:.3px;color:#222}
  .spread-label.underlined{text-decoration:underline}
  .panel-label{position:absolute;top:1091px;width:187px;text-align:center;font-size:13px;color:#222}

  .spread{position:absolute;top:650px;width:560px;height:433px;display:flex;box-shadow:0 2px 8px rgba(0,0,0,.15)}
  .spread.outside{left:37px}
  .spread.inside{left:617px}
  .panel{position:relative;width:187px;height:433px;background:var(--cream);overflow:hidden}

  .photo{position:absolute;left:0;width:100%}
  .wordmark{position:absolute;left:0;width:100%;text-align:center;color:var(--white)}
  .wordmark .name{font-family:"Playfair Display",Georgia,serif;font-weight:700;font-size:23px;letter-spacing:4px;line-height:1}
  .wordmark .sub{font-size:8px;letter-spacing:6px;margin-top:5px}
  .wordmark.brand{color:var(--brand)}

  .copy{position:absolute;left:17px;right:13px;font-size:7.3px;line-height:1.33}
  .copy h3{font-size:8.4px;font-weight:700;margin-bottom:2px;color:var(--brand-deep)}
  .copy p+p{margin-top:7px}

  .band{position:absolute;left:0;bottom:0;width:100%;color:var(--white);padding:7px 12px;font-size:5.5px;line-height:1.35}
  .band h4{font-size:6px;font-weight:700;margin-bottom:1px}

  /* back panel */
  .info{position:absolute;top:88px;width:100%;text-align:center;color:var(--brand);font-size:11px;line-height:1.3}
  .info p+p{margin-top:14px}
  .map{top:207px;height:168px;background:linear-gradient(135deg,#f1efe9,#e3e8e4 60%,#f3ead8)}
  .contact{position:absolute;left:0;bottom:0;width:100%;height:58px;background:var(--brand-deep);color:var(--white);text-align:center;padding-top:6px}
  .contact .phone{font-size:20px}
  .contact .visit{font-size:10px;margin-top:2px}

  /* cover */
  .cover-art{position:absolute;inset:10px 8px 10px 8px;background:linear-gradient(165deg,#2f6fb3 0%,#8fb2d8 48%,var(--cream) 100%)}
  .icon-stack{position:absolute;left:70px;top:99px;display:flex;flex-direction:column;gap:8px}
  .icon-dot{width:47px;height:47px;border-radius:50%;display:flex;align-items:center;justify-content:center}
  .icon-dot svg{width:24px;height:24px;fill:none;stroke:var(--white);stroke-width:1.6;stroke-linecap:round;stroke-linejoin:round}
  .tagline{position:absolute;left:40px;top:358px;width:112px;background:var(--cream);text-align:center;color:var(--brand);padding:3px 0}
  .tagline .t1{font-size:10px;letter-spacing:.5px}
  .tagline .t2{font-size:8px}
  .cover-url{position:absolute;left:0;width:100%;top:404px;text-align:center;font-size:8px;color:var(--brand)}

  .topbar{position:absolute;top:0;left:0;width:100%;height:8px}
</style>
</head>
<body>

<div class="spread-label underlined" style="left:264px">OUTSIDE PANELS</div>
<div class="spread-label" style="left:845px">INSIDE PANELS</div>

<section class="spread outside">
  <article class="panel">
    <div class="photo" role="img" aria-label="Photo of a bright clinical room with modern imaging equipment" style="top:0;height:155px;background:linear-gradient(160deg,var(--brand-deep) 0%,#4f82bd 45%,#dfe6ef 100%)"></div>
    <div class="wordmark" style="top:22px"><div class="name">MARLOW</div><div class="sub">FINANCE</div></div>
    <div class="copy" style="top:161px">
      <h3>Marlow Finance</h3>
      <p>With over 30 years in the finance industry, the experienced team at Marlow Finance are dedicated to helping our clients locate the best solution to fulfill their financial needs. With the recent changes to both commercial and consumer lending, it's vital that you find a broker who will protect your credit rating and help you to make the best decision for your situation.</p>
      <p>Our extensive and exclusive portfolio of financial lenders gives the team at Marlow Finance the ability to be highly selective and prioritise our client's best interests. Selecting the right finance package can help our client's save a significant time and money.</p>
    </div>
    <div class="band" style="background:var(--brand-deep);height:58px">
      <h4>Finance Kept Simple</h4>
      For more information on how Marlow Finance can help you to find the best financial solution for your needs, speak to one of our consultants today.
    </div>
  </article>

  <article class="panel">
    <div class="wordmark brand" style="top:22px"><div class="name">MARLOW</div><div class="sub">FINANCE</div></div>
    <div class="info">
      <p>HOURS OF OPERATION<br>MON-FRI 8:30am - 5:30pm<br>SAT 8:30am - 12noon</p>
      <p>OFFICE ADDRESS<br>42 Harrow Lane Ascot<br>QLD 4011</p>
    </div>
    <div class="photo map" role="img" aria-label="Street map showing the office location"></div>
    <div class="contact">
      <div class="phone">(07) 3000 0199</div>
      <div class="visit">visit us marlowfinance.com.au</div>
    </div>
  </article>

  <article class="panel">
    <div class="cover-art" role="img" aria-label="Soft blue-tinted photo of a clinical imaging room"></div>
    <div class="wordmark" style="top:38px"><div class="name">MARLOW</div><div class="sub">FINANCE</div></div>
    <div class="icon-stack">
      <div class="icon-dot" style="background:var(--brand-deep)">
        <svg viewBox="0 0 24 24"><rect x="5" y="3" width="12" height="17" rx="1"/><path d="M8 8h6M8 12h6M8 16h4"/></svg>
      </div>
      <div class="icon-dot" style="background:var(--brand-light)">
        <svg viewBox="0 0 24 24"><path d="M3 15v-3l3-4h10l4 4v3z"/><circle cx="7.5" cy="16" r="1.8"/><circle cx="16.5" cy="16" r="1.8"/></svg>
      </div>
      <div class="icon-dot" style="background:var(--brand-mid)">
        <svg viewBox="0 0 24 24"><rect x="3" y="11" width="11" height="5"/><path d="M14 13l4-6 3 3"/><circle cx="6" cy="18" r="1.5"/><circle cx="11" cy="18" r="1.5"/></svg>
      </div>
      <div class="icon-dot" style="background:var(--brand)">
        <svg viewBox="0 0 24 24"><path d="M4 11l8-7 8 7"/><path d="M6 10v10h12V10"/><path d="M10 20v-5h4v5"/></svg>
      </div>
    </div>
    <div class="tagline"><div class="t1">READ INSIDE TO</div><div class="t2">KEEP THINGS SIMPLE</div></div>
    <div class="cover-url">marlowfinance.com.au</div>
  </article>
</section>

<section class="spread inside">
  <article class="panel">
    <div class="photo" role="img" aria-label="Photo of a dark teal sports car in a studio" style="top:0;height:176px;background:linear-gradient(160deg,#2a3034,#4d5a5e 55%,#1f5a5c)"></div>
    <div class="topbar" style="background:var(--brand-light)"></div>
    <div class="wordmark" style="top:18px"><div class="name">MARLOW</div><div class="sub">CARS</div></div>
    <div class="copy" style="top:190px;left:25px">
      <h3>Vehicle Sourcing Specialists</h3>
      <p>With over 30 years in the automotive industry, the team at Marlow Cars has the negotiating skills to achieve the best outcomes for our clients. Marlow Cars is your car solutions specialist. Our experienced team will source the vehicle of your choice, handle any trade in you need to dispose of, assist with the financing and have the vehicle delivered to your door.</p>
    </div>
    <div class="band" style="background:var(--brand-light);height:75px">
      <h4>Vehicle Purchasing Kept Simple</h4>
      Marlow Cars is your vehicle solution specialist. Let us take the stress out of buying your next car by simply sending us your contact details, and one of our vehicle specialists will call to discuss your requirements. Our expert negotiators are ready to get to work on your behalf.
    </div>
  </article>

  <article class="panel">
    <div class="photo" role="img" aria-label="Photo of a yellow wheel loader on a gravel site" style="top:0;height:176px;background:linear-gradient(170deg,#8fa9c4 0%,#c7c2b0 50%,#8a7a55 100%)"></div>
    <div class="topbar" style="background:var(--brand)"></div>
    <div class="wordmark" style="top:18px"><div class="name">MARLOW</div><div class="sub">EQUIPMENT</div></div>
    <div class="copy" style="top:190px;left:27px">
      <h3>Marlow Equipment Finance</h3>
      <p>With over 30 years in the finance industry, the team at Marlow Equipment have all the resources to help our commercial clients select the best equipment finance facility for their situation. The recent changes to the financial markets, make it imperative that commercial clients find an experienced broker who has their client's best interests as a priority.</p>
    </div>
    <div class="band" style="background:var(--brand);height:75px">
      <h4>Equipment Finance Kept Simple</h4>
      Marlow Equipment is your equipment finance solution specialist. With an extensive and exclusive portfolio of financial lenders, the team at Marlow Equipment will help you to identify your best options, whilst protecting your business. Contact us today and our expert negotiators will help to find the best financial solution for your situation.
    </div>
  </article>

  <article class="panel">
    <div class="photo" role="img" aria-label="Dusk photo of a modern home with a pool" style="top:0;height:176px;background:linear-gradient(170deg,#2f4a6b 0%,#5f7895 50%,#c9b79a 100%)"></div>
    <div class="topbar" style="background:var(--brand-deep)"></div>
    <div class="wordmark" style="top:18px"><div class="name">MARLOW</div><div class="sub">MORTGAGES</div></div>
    <div class="copy" style="top:190px;left:26px">
      <h3>Home Loan Specialists</h3>
      <p>With over 30 years in the finance industry, the team at Marlow Mortgages have the experience to help our clients source the best home loan for their situation. The recent changes to the finance and banking industry and a strong focus on the capacity to repay a loan, means that the assistance of a broker is vital to protecting your credit score.</p>
    </div>
    <div class="band" style="background:var(--brand-deep);height:75px">
      <h4>Home Loan Finance Kept Simple</h4>
      Marlow Mortgages is your home loan solution specialist. With an extensive and exclusive portfolio of lenders through our referral partners, we assist you to identify the best options to help you save a significant amount of interest over the life of your loan. Contact us today and our expert negotiators will help you to find the best mortgage options for your situation.
    </div>
  </article>
</section>

<div class="panel-label" style="left:31px">FOLDED INSIDE PANEL</div>
<div class="panel-label" style="left:238px">OUTSIDE BACK</div>
<div class="panel-label" style="left:412px">COVER</div>
<div class="panel-label" style="left:609px">INSIDE PANEL 1</div>
<div class="panel-label" style="left:797px">INSIDE PANEL 2</div>
<div class="panel-label" style="left:984px">INSIDE PANEL 3</div>

</body>
</html>
```